Stationery Design Project

We need a Stationery Design for automotive industry.

Target Market(s)

Mechanic garage and Mechanics

Industry/Entity Type

Automotive

Requirements
Must have
• The logo company and the legal information.

We are a car spart parts and tools delar
Nice to have
• We like something elegant and simple.

```html
<!DOCTYPE html>
<html lang="en">
<head>
<meta charset="utf-8">
<title>Northline Motor Parts – Stationery Set</title>
<link rel="stylesheet" href="https://fonts.googleapis.com/css2?family=Didact+Gothic&display=swap">
<style>
  :root{
    --stage:#3b3b3b;
    --paper:#ffffff;
    --ink:#0d0d0d;
    --ink-soft:#1a1a1a;
    --steel:#8a8a8a;
    --blue:#3d6bb8;
    --blue-light:#5b86cf;
    --ghost:#d2d2d2;
    --text:#222222;
  }
  html,body{margin:0;padding:0;width:1200px;height:981px;overflow:hidden;background:var(--stage);}
  .stationery-set{display:block;width:1200px;height:981px;font-family:"Didact Gothic",sans-serif;}
  .brand-name{font-family:"Didact Gothic",sans-serif;fill:#ffffff;letter-spacing:1px;}
  .contact-light{font-family:"Didact Gothic",sans-serif;fill:#ffffff;}
  .contact-dark{font-family:"Didact Gothic",sans-serif;fill:var(--text);}
  .contact-link{fill:var(--blue-light);}
  .address-rule{stroke:var(--ink);stroke-width:1;}
  .swoosh-line{fill:none;stroke:var(--blue);stroke-width:1.2;}
  .blue-band{fill:var(--blue);}
  .dot{fill:var(--blue);}
</style>
</head>
<body>
<svg class="stationery-set" viewBox="0 0 1170 956" width="1200" height="981" xmlns="http://www.w3.org/2000/svg">
  <defs>
    <linearGradient id="steel-fade" x1="0" y1="0" x2="1" y2="0">
      <stop offset="0" stop-color="#0d0d0d"/>
      <stop offset="0.55" stop-color="#2a2a2a"/>
      <stop offset="0.8" stop-color="#8a8a8a"/>
      <stop offset="1" stop-color="#1a1a1a"/>
    </linearGradient>
    <linearGradient id="dark-sheen" x1="0" y1="0" x2="1" y2="1">
      <stop offset="0" stop-color="#000"/>
      <stop offset="0.6" stop-color="#1c1c1c"/>
      <stop offset="1" stop-color="#6e6e6e"/>
    </linearGradient>
    <radialGradient id="hub-silver" cx="0.5" cy="0.5" r="0.5">
      <stop offset="0.55" stop-color="#f4f4f4"/>
      <stop offset="0.8" stop-color="#9a9a9a"/>
      <stop offset="1" stop-color="#dcdcdc"/>
    </radialGradient>
    <clipPath id="clip-letterhead-band"><rect x="422" y="62" width="596" height="86"/></clipPath>
    <clipPath id="clip-envelope"><rect x="18" y="238" width="623" height="312"/></clipPath>
    <clipPath id="clip-disc"><circle cx="995" cy="362" r="160"/></clipPath>
    <clipPath id="clip-card-front"><rect x="320" y="590" width="257" height="142"/></clipPath>
  </defs>

  <!-- Letterhead -->
  <g class="letterhead">
    <rect x="422" y="62" width="596" height="843" fill="var(--paper)"/>
    <g clip-path="url(#clip-letterhead-band)">
      <rect x="422" y="62" width="596" height="86" fill="url(#dark-sheen)"/>
      <path d="M422,62 C560,100 700,110 1018,80 L1018,62 Z" fill="#151515"/>
      <path d="M960,62 C985,90 990,120 985,148 L1000,148 C1005,118 995,85 975,62 Z" class="blue-band"/>
      <path d="M950,62 C975,90 980,120 972,148" class="swoosh-line"/>
      <circle class="dot" cx="958" cy="86" r="2"/><circle class="dot" cx="963" cy="99" r="2"/><circle class="dot" cx="966" cy="112" r="2"/>
    </g>
    <text class="brand-name" x="597" y="112" font-size="11" text-anchor="middle">NORTHLINE MOTOR PARTS</text>
    <g class="contact-light" font-size="9.5" text-anchor="end">
      <text x="943" y="84">Northline Motor Parts Pty Ltd.</text>
      <text x="943" y="96">ABN:48 302 579 114</text>
      <text x="951" y="107">P.O. 402 Marrickville 2204 SYDNEY NSW.</text>
      <text x="955" y="118">PHONE:0400 512 338</text>
      <text x="958" y="129">info@northlinemotor.com.au</text>
      <text x="962" y="140" class="contact-link">www.northlinemotor.com.au</text>
    </g>
  </g>

  <!-- Envelope -->
  <g class="envelope">
    <rect x="18" y="238" width="623" height="312" fill="var(--paper)" stroke="#9a9a9a" stroke-width="0.8"/>
    <g clip-path="url(#clip-envelope)">
      <path d="M18,238 L70,238 C10,300 20,470 300,550 L18,550 Z" fill="url(#steel-fade)"/>
      <path d="M70,238 L110,238 C40,300 60,460 312,550 L290,550 C30,470 5,310 70,238 Z" class="blue-band"/>
      <path d="M138,238 C60,300 80,470 320,550" class="swoosh-line"/>
    </g>
    <ellipse cx="502" cy="312" rx="110" ry="45" fill="var(--ink)"/>
    <text class="brand-name" x="502" y="316" font-size="12" text-anchor="middle">NORTHLINE MOTOR PARTS</text>
    <g class="contact-dark" font-size="11">
      <text x="78" y="363">Northline Motor Parts Pty Ltd.</text>
      <text x="87" y="375">ABN:48 302 579 114</text>
      <text x="97" y="387">P.O. 402 Marrickville 2204 SYDNEY NSW.</text>
      <text x="107" y="399">PHONE:0400 512 338</text>
      <text x="117" y="411">www.northlinemotor.com.au</text>
      <text x="127" y="423">info@northlinemotor.com.au</text>
    </g>
    <circle class="dot" cx="73" cy="361" r="2.2"/><circle class="dot" cx="77" cy="376" r="2.2"/><circle class="dot" cx="83" cy="391" r="2.2"/><circle class="dot" cx="91" cy="405" r="2.2"/>
    <g class="address-lines">
      <line class="address-rule" x1="303" y1="427" x2="593" y2="427"/>
      <line class="address-rule" x1="303" y1="446" x2="593" y2="446"/>
      <line class="address-rule" x1="303" y1="465" x2="593" y2="465"/>
      <line class="address-rule" x1="303" y1="484" x2="593" y2="484"/>
      <line class="address-rule" x1="303" y1="503" x2="593" y2="503"/>
    </g>
  </g>

  <!-- Faint brand mark -->
  <g class="brand-ghost">
    <ellipse cx="723" cy="497" rx="150" ry="50" fill="var(--ghost)"/>
    <text class="brand-name" x="723" y="503" font-size="16" text-anchor="middle">NORTHLINE MOTOR PARTS</text>
  </g>

  <!-- Disc -->
  <g class="disc">
    <circle cx="995" cy="362" r="164" fill="#e8e8e8" stroke="#bcbcbc"/>
    <g clip-path="url(#clip-disc)">
      <rect x="830" y="198" width="330" height="330" fill="var(--ink)"/>
      <path d="M870,200 C1000,210 1100,225 1160,230 L1160,330 C1100,280 1000,250 900,240 Z" fill="#3a3a3a" opacity="0.7"/>
      <path d="M880,240 C830,330 880,470 1160,520 L1160,528 L830,528 L830,240 Z" fill="url(#steel-fade)"/>
      <path d="M870,250 C820,360 900,490 1160,515 L1160,470 C930,460 850,360 900,240 Z" class="blue-band"/>
      <path d="M905,225 C850,330 900,470 1160,500" class="swoosh-line"/>
    </g>
    <ellipse cx="987" cy="278" rx="65" ry="22" fill="#1f1f1f"/>
    <text class="brand-name" x="987" y="282" font-size="8" text-anchor="middle">NORTHLINE MOTOR PARTS</text>
    <circle cx="995" cy="362" r="60" fill="url(#hub-silver)"/>
    <circle cx="995" cy="362" r="40" fill="#e9e9e9" stroke="#c4c4c4"/>
    <circle cx="995" cy="362" r="30" fill="none" stroke="#cfcfcf"/>
    <circle cx="995" cy="362" r="15" fill="#ffffff" stroke="#bdbdbd"/>
    <g class="contact-light" font-size="7.5">
      <text x="973" y="434">Northline Motor Parts Pty Ltd.</text>
      <text x="979" y="443">ABN:48 302 579 114</text>
      <text x="986" y="452">P.O. 402 Marrickville 2204 SYDNEY NSW.</text>
      <text x="993" y="461">PHONE:0400 512 338</text>
      <text x="999" y="470" class="contact-link">www.northlinemotor.com.au</text>
      <text x="1006" y="478" class="contact-link">info@northlinemotor.com.au</text>
    </g>
  </g>

  <!-- Business card front -->
  <g class="card-front">
    <rect x="320" y="590" width="257" height="142" fill="var(--ink)"/>
    <g clip-path="url(#clip-card-front)">
      <path d="M320,590 L360,590 C330,640 360,700 420,732 L320,732 Z" fill="url(#steel-fade)"/>
      <path d="M355,590 L372,590 C345,650 380,710 470,732 L450,732 C370,710 335,650 355,590 Z" class="blue-band"/>
      <path d="M385,590 C355,650 395,715 500,732" class="swoosh-line"/>
      <path d="M420,590 L577,590 L577,640 C520,600 470,595 420,590 Z" fill="#2b2b2b"/>
      <path d="M540,700 L577,680 L577,732 L520,732 Z" fill="#4a4a4a" opacity="0.6"/>
    </g>
    <ellipse cx="506" cy="623" rx="60" ry="18" fill="#1a1a1a"/>
    <text class="brand-name" x="506" y="627" font-size="7" text-anchor="middle">NORTHLINE MOTOR PARTS</text>
    <text class="contact-light" x="372" y="655" font-size="11">Daniel Moreton</text>
    <text class="contact-light" x="469" y="663" font-size="7" text-anchor="end">Director</text>
    <g class="contact-light" font-size="6">
      <text x="393" y="683">Northline Motor Parts Pty Ltd.</text>
      <text x="405" y="691">ABN:48 302 579 114</text>
      <text x="414" y="699">P.O. 402 Marrickville 2204 SYDNEY NSW.</text>
      <text x="422" y="706">PHONE:0400 512 338</text>
      <text x="430" y="713">www.northlinemotor.com.au</text>
      <text x="449" y="720" class="contact-link">daniel@northlinemotor.com.au</text>
    </g>
  </g>

  <!-- Business card back -->
  <g class="card-back">
    <rect x="318" y="741" width="257" height="143" fill="#111111"/>
    <text class="brand-name" x="446" y="818" font-size="14" text-anchor="middle">NORTHLINE MOTOR PARTS</text>
  </g>
</svg>
</body>
</html>
```